American Ingenuity + Italian Design = RTB
International consulting services from fine arts/advertising/construction & special events. A new company that will find the right connections to get your job done.

Card should include -
1. Company Name with logo: rosalind tavera Enterprises LLC
2. Address: 218 Marlow Bend, Highland Springs, VA 23091
3. Phone Number: 804.555.2164 (US)
4. Tagline: American Ingenuity + Italian Style + RTB (you can improve on this idea)
5. web address to be added eventually

Likes: airplanes and boats to give the idea of movement & international ability
Logo: if you have an idea to adjust the colors, we are open to that. Rosalind likes blues, but other colors didn't seem to work; remember this will print 4c in most cases)
Updates

I have uploaded the logo on it's own. Typical business card size for the US is 3.5" x 2", but doesn't have to be that size. the flyer was just for reference of something else that was done and to give some background. I hope that didn't confuse anyone.

Thank you all for the amazing work in the tight deadline. We will be reviewing everything today and will provide feedback by tomorrow. I will also pass this site on to anyone I know looking for design work.

website address rosalindtavera.example email rosalind@rosalindtavera.example Italian number +39 333 581 0492 USA 1 804 555 2164 International Consulting Services American Ingenuity. Italian Design. rtB These are the vital elements for the card. In addition please note the new fotos should have been uploaded. Best Regards

Target Market(s)

Companies or individuals that want to bring the Italian flair to the US or American know how to Italian projects. This can range from a bride planning a destination wedding, an interior designer looking to add pieces or knowledge to their project, or an investor looking to buy property to invest and build.

Industry/Entity Type

Construction

Requirements
Must have
• 1. Company Name with logo: rosalind tavera Enterprises LLC
+39 333 581 0492 (Italia)
Nice to have
• incorporate the idea of international ability; airplanes (like the wing in the background of the logo)
Should not have
• not overly decorative

```html
<!DOCTYPE html>
<html lang="en">
<head>
<meta charset="utf-8">
<title>rosalind tavera Enterprises LLC — Business Card</title>
<link rel="stylesheet" href="https://fonts.googleapis.com/css2?family=Archivo:wght@700&family=Roboto+Condensed:wght@400&display=swap">
<style>
  :root {
    --page: #d9d9d9;
    --card-light: #efecea;
    --card-shade: #dcd7d4;
    --photo-warm: #cdbfb8;
    --photo-pale: #e6dfdb;
    --photo-grey: #b9b0ab;
    --brand: #7b2b1f;
    --ink: #141414;
    --ghost: rgba(120, 105, 100, 0.16);
    --edge: rgba(0, 0, 0, 0.12);
  }
  * { box-sizing: border-box; margin: 0; padding: 0; }
  html, body {
    width: 1200px;
    height: 1200px;
    overflow: hidden;
    background: var(--page);
  }
  .sheet {
    width: 1200px;
    height: 1200px;
    display: flex;
    flex-direction: column;
    align-items: center;
    justify-content: center;
    gap: 80px;
  }
  .card {
    position: relative;
    width: 840px;
    height: 480px;
    overflow: hidden;
    box-shadow: 0 2px 10px var(--edge);
  }

  /* Brand lockup: name with a plain circle mark */
  .brand {
    display: flex;
    align-items: center;
    justify-content: center;
    gap: 16px;
    font-family: "Roboto Condensed", sans-serif;
    font-weight: 400;
    color: var(--brand);
    white-space: nowrap;
  }
  .brand-mark {
    flex: none;
    border-radius: 50%;
    background: var(--brand);
  }

  /* Logo side */
  .cover-photo {
    position: absolute;
    inset: 0;
    background:
      linear-gradient(200deg, var(--photo-pale) 0%, rgba(230,223,219,0) 45%),
      linear-gradient(160deg, var(--photo-grey) 0%, var(--photo-warm) 40%, var(--photo-pale) 75%, var(--photo-warm) 100%);
  }
  .card--cover .brand {
    position: absolute;
    left: 0;
    right: 0;
    top: 200px;
    font-size: 52px;
  }
  .card--cover .brand-mark { width: 36px; height: 36px; }

  /* Contact side */
  .card--contact {
    background: linear-gradient(170deg, var(--card-light) 0%, var(--card-light) 55%, var(--card-shade) 100%);
  }
  .contact-photo {
    position: absolute;
    left: 0;
    top: 40px;
    width: 420px;
    height: 300px;
    background: linear-gradient(150deg, rgba(185,176,171,0.35) 0%, rgba(205,191,184,0.15) 60%, rgba(239,236,234,0) 100%);
  }
  .ghost-name {
    position: absolute;
    left: 40px;
    bottom: 22px;
    font-family: "Roboto Condensed", sans-serif;
    font-weight: 400;
    font-size: 54px;
    color: var(--ghost);
    white-space: nowrap;
  }
  .contact-block {
    position: absolute;
    left: 170px;
    top: 58px;
    width: 580px;
    text-align: center;
  }
  .contact-block .brand {
    font-size: 32px;
    margin-bottom: 22px;
  }
  .contact-block .brand-mark { width: 22px; height: 22px; gap: 12px; }
  .tagline {
    font-family: "Archivo", sans-serif;
    font-weight: 700;
    font-size: 21px;
    color: var(--ink);
    margin-bottom: 8px;
  }
  .contact-line {
    font-family: "Roboto Condensed", sans-serif;
    font-weight: 400;
    font-size: 21px;
    color: var(--ink);
    line-height: 1.35;
  }
</style>
</head>
<body>
  <main class="sheet">
    <section class="card card--cover">
      <div class="cover-photo" role="img" aria-label="Soft faded photo of an airplane wing above a boat deck, suggesting international travel"></div>
      <p class="brand"><span class="brand-mark"></span>rosalind tavera Enterprises LLC</p>
    </section>

    <section class="card card--contact">
      <div class="contact-photo" role="img" aria-label="Faint faded photo of an airplane wing and boat railing"></div>
      <p class="ghost-name" aria-hidden="true">rosalind tavera Enterprises LLC</p>
      <div class="contact-block">
        <p class="brand"><span class="brand-mark"></span>rosalind tavera Enterprises LLC</p>
        <p class="tagline">American Ingenuity + Italian Style + RTB</p>
        <p class="contact-line">218 Marlow Bend, Highland Springs, VA 23091</p>
        <p class="contact-line">804.555.2164 (US)</p>
        <p class="contact-line">+39 333 581 0492 (Italia)</p>
        <p class="contact-line">rosalindtavera.example</p>
        <p class="contact-line">rosalind@rosalindtavera.example</p>
      </div>
    </section>
  </main>
</body>
</html>
```